After tattoo calming solution

The label has to be modern, along the same lines as skin care brand “Dew Harbor.” It has to reflect the solutions natural effectiveness and simplicity. The label cannot be over fussy, and must be a little bit clinical, as it really does work. The colours should reflect that the solution calms the skin.

We use a 100ml spray bottle.

Target Market(s)

Anyone with a new tattoo or piercing

Industry/Entity Type

Skincare

Requirements
Must have
• Must reflect its natural calming but still remain a little clinical
Should not have
• It must not look like other flowery tattoo cream solutions.

```html
<!DOCTYPE html>
<html lang="en">
<head>
<meta charset="UTF-8">
<title>After Tattoo &amp; Piercing – Label</title>
<link rel="stylesheet" href="https://fonts.googleapis.com/css2?family=Montserrat:wght@200;300;600;700&display=swap">
<style>
  :root {
    --page-bg: #f5f5f5;
    --teal-deep: #17b8aa;
    --teal-light: #74ddd4;
    --teal-mid: #2fb3a5;
    --teal-edge: #46b5aa;
    --label-text: #ffffff;
    --ornament-tone: rgba(20, 130, 120, 0.28);
  }
  * { margin: 0; padding: 0; box-sizing: border-box; }
  html, body {
    width: 900px;
    height: 1200px;
    overflow: hidden;
    background: var(--page-bg);
    font-family: "Montserrat", sans-serif;
  }
  .canvas {
    position: relative;
    width: 900px;
    height: 1200px;
  }
  .label {
    position: absolute;
    left: 105px;
    top: 20px;
    width: 690px;
    height: 1160px;
    background: linear-gradient(90deg,
      var(--teal-deep) 0%,
      var(--teal-light) 30%,
      var(--teal-mid) 62%,
      var(--teal-edge) 100%);
    color: var(--label-text);
    overflow: hidden;
  }
  .product-name {
    position: absolute;
    left: 50px;
    top: 120px;
    font-weight: 200;
    font-size: 124px;
    line-height: 118px;
    letter-spacing: 2px;
  }
  .product-name .line { display: block; }
  .product-sub {
    position: absolute;
    left: 52px;
    top: 355px;
    font-weight: 700;
    font-size: 78px;
    line-height: 1;
  }
  .accent-bar {
    position: absolute;
    left: 52px;
    top: 601px;
    width: 8px;
    height: 190px;
    background: var(--label-text);
  }
  .tagline {
    position: absolute;
    left: 82px;
    top: 616px;
    font-weight: 600;
    font-size: 49px;
    line-height: 63px;
    letter-spacing: 1.5px;
  }
  .benefits {
    position: absolute;
    left: 50px;
    top: 838px;
    font-weight: 300;
    font-size: 35px;
    line-height: 45px;
    letter-spacing: 1px;
  }
  .volume {
    position: absolute;
    left: 50px;
    top: 1046px;
    font-weight: 300;
    font-size: 34px;
  }
  .ornament-column {
    position: absolute;
    left: 591px;
    top: 17px;
    width: 92px;
    height: 1130px;
    background: var(--ornament-tone);
    border-radius: 6px;
  }
</style>
</head>
<body>
  <main class="canvas">
    <section class="label">
      <h1 class="product-name">
        <span class="line">AFTER</span>
        <span class="line">TATTOO</span>
      </h1>
      <p class="product-sub">&amp; Piercing</p>

      <div class="accent-bar"></div>
      <p class="tagline">Expert skin repair<br>for new tattoos<br>&amp; piercings</p>

      <p class="benefits">Reduces inflammation,<br>irritation and encourages<br>natural skin healing</p>

      <p class="volume">100 mL</p>

      <div class="ornament-column" role="img" aria-label="Vertical row of line-drawn tattoo flash icons: dagger, swallow, eye, diamond, heart with arrow, star, anchor"></div>
    </section>
  </main>
</body>
</html>
```